Biz Card Design TPVC

New business card for a new company.
Logo was completed by a designer on ArtFlock and looking to continue requesting additional services.
Company Name: Tidal Prime Voltage Collective
Although this company is starting in Canada, we will be moving towards a global presence within the next 6 months.
Key elements to this business are as follows.
Energy Procurement
Energy Reduction Services
Demand Side Consulting
Energy Efficiency Consulting
Saving Clients Money
Helping Them Go "Green"
Managing Their Energy Requirements
Basically the goal for our company is to find the best procurement solution for our clients and reduce their energy consumption. This reduces their expenses and the amount of greenhouse gas they produce on a daily basis.
I have been in the energy footprint for the last 20 years and know that most companies are looking to "do whatever is necessary to get them to sign on the dotted line". I would prefer to walk away from a client that I can't help than to put them into a situation that they will regret for years to come. This is where the "TIDAL" part of the company name comes from.
The following is a catch phrase that encompasses what we do.
"Reducing your carbon footprint & energy bill at the same time!"
The back of the card needs to have this statement along with some sort of illustration. The back is a playground for creative ideas.
The front of the card needs the following.
Logo.
First & Last Name (Gus Marwick)
Title (Energy Warrior)
Phone Number (555) 314-2768
Fax Number (555) 862-4091
Email Address gus@tidalprimevoltage.example
Address 47 Orchard Lane Toronto Ontario K4P 2Z7
I want it to be a card that is remembered when any of my staff give it to a customer. It HAS to stand out.
Target Market(s)
Business Owners, Decision Makers, 30 to 65+
Industry/Entity Type
Business
Look and feel
Each slider illustrates characteristics of the customer's brand and the style your logo design should communicate.

```html
<!DOCTYPE html>
<html lang="en">
<head>
<meta charset="utf-8">
<title>Tidal Prime Voltage Collective – Business Card</title>
<link rel="stylesheet" href="https://fonts.googleapis.com/css2?family=Lato:wght@400;700&family=Roboto+Condensed:ital,wght@1,700&display=swap">
<style>
  :root {
    --canvas: #e6e9ec;
    --card: #ffffff;
    --brand-blue: #3b63b3;
    --brand-green: #5aae3c;
    --ink: #2b2b2b;
    --ink-soft: #5a5a5a;
    --icon-blue: #3f6fb8;
    --band-green: #b6e6a8;
    --tagline-ink: #1f2a1c;
    --watermark: rgba(90, 174, 60, 0.13);
    --photo-coin: #d9ccb3;
    --photo-leaf: #4f8f2e;
    --photo-light: #f3efe6;
  }
  * { box-sizing: border-box; margin: 0; padding: 0; }
  html, body { width: 1200px; height: 960px; overflow: hidden; }
  body {
    background: var(--canvas);
    font-family: "Lato", sans-serif;
    color: var(--ink);
    display: flex;
    flex-direction: column;
    align-items: center;
    justify-content: center;
    gap: 56px;
  }
  .card {
    position: relative;
    width: 700px;
    height: 400px;
    background: var(--card);
    border-radius: 64px 10px 64px 10px;
    overflow: hidden;
    box-shadow: 0 6px 18px rgba(0,0,0,0.15);
  }

  /* Front */
  .watermark {
    position: absolute;
    left: 440px;
    top: 70px;
    width: 320px;
    height: 320px;
    border-radius: 50%;
    background: var(--watermark);
  }
  .brand {
    position: absolute;
    top: 70px;
    left: 40px;
    display: flex;
    align-items: center;
    gap: 12px;
  }
  .brand-dot {
    width: 22px; height: 22px;
    border-radius: 50%;
    background: var(--brand-green);
  }
  .brand-name {
    font-weight: 700;
    font-size: 30px;
    letter-spacing: -0.3px;
    color: var(--brand-blue);
  }
  .person-name {
    position: absolute;
    top: 172px;
    left: 40px;
    font-size: 34px;
    font-weight: 400;
    letter-spacing: 0.5px;
    text-transform: uppercase;
  }
  .person-title {
    position: absolute;
    top: 218px;
    left: 41px;
    font-size: 17px;
    color: var(--ink-soft);
    letter-spacing: 0.3px;
  }
  .contact-list {
    position: absolute;
    left: 40px;
    bottom: 36px;
    list-style: none;
    font-size: 20px;
    line-height: 30px;
  }
  .contact-list li, .address {
    display: flex;
    align-items: center;
    gap: 12px;
  }
  .contact-icon { width: 18px; height: 18px; flex: none; }
  .address {
    position: absolute;
    right: 40px;
    top: 228px;
    align-items: flex-start;
    font-size: 19px;
    line-height: 26px;
  }
  .address .contact-icon { margin-top: 4px; }

  /* Back */
  .back-photo {
    position: absolute;
    top: 0; right: 0;
    width: 62%;
    height: 100%;
    background:
      radial-gradient(ellipse at 50% 45%, var(--photo-leaf) 0%, #6fa84a 28%, rgba(111,168,74,0) 55%),
      linear-gradient(135deg, var(--photo-light) 0%, var(--photo-coin) 55%, #c8b99c 100%);
  }
  .tagline-band {
    position: absolute;
    top: 92px;
    left: 38px;
    width: 360px;
    padding: 10px 16px;
    background: var(--band-green);
    font-family: "Roboto Condensed", sans-serif;
    font-style: italic;
    font-weight: 700;
    font-size: 22px;
    line-height: 26px;
    color: var(--tagline-ink);
  }
</style>
</head>
<body>

  <section class="card card-front" aria-label="Business card front">
    <div class="watermark" aria-hidden="true"></div>

    <div class="brand">
      <span class="brand-dot"></span>
      <span class="brand-name">Tidal Prime Voltage Collective</span>
    </div>

    <h1 class="person-name">Gus Marwick</h1>
    <p class="person-title">Energy Warrior</p>

    <ul class="contact-list">
      <li>
        <svg class="contact-icon" viewBox="0 0 18 18" aria-label="Phone">
          <rect x="4" y="1" width="10" height="16" rx="2" fill="none" stroke="var(--icon-blue)" stroke-width="2"/>
          <line x1="7" y1="14" x2="11" y2="14" stroke="var(--icon-blue)" stroke-width="2"/>
        </svg>
        (555) 314-2768
      </li>
      <li>
        <svg class="contact-icon" viewBox="0 0 18 18" aria-label="Fax">
          <rect x="4" y="1" width="10" height="5" fill="var(--icon-blue)"/>
          <rect x="1" y="6" width="16" height="8" rx="1" fill="var(--icon-blue)"/>
          <rect x="4" y="11" width="10" height="6" fill="#fff" stroke="var(--icon-blue)" stroke-width="1.5"/>
        </svg>
        (555) 862-4091
      </li>
      <li>
        <svg class="contact-icon" viewBox="0 0 18 18" aria-label="Email">
          <rect x="1" y="3" width="16" height="12" fill="none" stroke="var(--icon-blue)" stroke-width="1.6"/>
          <polyline points="1,3 9,10 17,3" fill="none" stroke="var(--icon-blue)" stroke-width="1.6"/>
        </svg>
        gus@tidalprimevoltage.example
      </li>
    </ul>

    <div class="address">
      <svg class="contact-icon" viewBox="0 0 18 18" aria-label="Address">
        <path d="M9 1a6 6 0 0 0-6 6c0 4.5 6 10 6 10s6-5.5 6-10a6 6 0 0 0-6-6z" fill="var(--icon-blue)"/>
        <circle cx="9" cy="7" r="2.2" fill="#fff"/>
      </svg>
      <span>47 Orchard Lane<br>Toronto Ontario K4P 2Z7</span>
    </div>
  </section>

  <section class="card card-back" aria-label="Business card back">
    <div class="back-photo" role="img" aria-label="Photo of a young green seedling growing from an energy-saving bulb on leaves over a pile of coins"></div>
    <p class="tagline-band">Reducing your carbon footprint &amp; energy bill at the same time!</p>
  </section>

</body>
</html>
```